Label for moisturizing face lotion - skin care

I need a label for a face moisturizer. Please see the details in the attachments. I also attached two variations of the logo.
The fonts are Futura PT for body
Orpheus Pro for header

We are looking for something very modern, simple, just black and white. It's an all natural product.
Please add under the logo:
with Phytoplankton extract and hyaluronic acid

Target Market(s)

Women

Industry/Entity Type

Skin care

Font styles to use
Sans Serif
Other font styles liked:
• Futura PT for body Orpheus Pro for header

Colors

Designer to choose only greyscale colors for use in the design.

Requirements
Nice to have
• White label with black letters, simple, clean, no serifs

```html
<!DOCTYPE html>
<html lang="en">
<head>
<meta charset="utf-8">
<title>ALVA Anti-Aging Moisturizer – Jar Label</title>
<link rel="stylesheet" href="https://fonts.googleapis.com/css2?family=Jost:ital,wght@0,400;0,500;0,600;1,400&family=Cormorant+Garamond:wght@500&family=Oswald:wght@300&display=swap">
<style>
  :root {
    --paper: #ffffff;
    --ink: #111111;
    --cut-line: #e3262b;
    --safe-line: #6b6b6b;
  }
  html, body {
    margin: 0;
    width: 1200px;
    height: 848px;
    overflow: hidden;
    background: var(--paper);
  }
  .label-sheet {
    position: absolute;
    left: 20px;
    top: 298px;
    width: 1160px;
    height: 252px;
  }
  .cut-line { fill: none; stroke: var(--cut-line); stroke-width: 3; }
  .safe-line { fill: none; stroke: var(--safe-line); stroke-width: 1.5; stroke-dasharray: 9 6; }
  .label-frame { fill: none; stroke: var(--ink); stroke-width: 4; }
  .info-box { fill: none; stroke: var(--ink); stroke-width: 2; }
  .body-text { font-family: "Jost", sans-serif; fill: var(--ink); }
  .maker-title { font-size: 19px; font-weight: 600; }
  .maker-line { font-size: 18px; font-weight: 400; }
  .exp-label { font-size: 15px; font-style: italic; }
  .benefit { font-size: 22px; font-weight: 400; }
  .brand-by { font-size: 6px; font-weight: 600; letter-spacing: 2px; }
  .product-name { font-family: "Cormorant Garamond", serif; font-weight: 500; font-size: 66px; letter-spacing: 6px; fill: var(--ink); }
  .product-type { font-size: 11px; font-weight: 500; letter-spacing: 2.4px; }
  .net-weight { font-family: "Cormorant Garamond", serif; font-size: 20px; fill: var(--ink); }
  .made-with { font-size: 11px; letter-spacing: 2.6px; }
  .key-extract { font-size: 12.5px; font-weight: 600; letter-spacing: 3px; }
  .ingredients { font-family: "Oswald", sans-serif; font-weight: 300; font-size: 18px; fill: var(--ink); }
  .brand-ring { fill: none; stroke: var(--ink); stroke-width: 1.5; }
</style>
</head>
<body>
<svg class="label-sheet" viewBox="225 130 1795 390" xmlns="http://www.w3.org/2000/svg">
  <!-- die cut -->
  <path class="cut-line" d="M282 163 Q1120 133 1962 163 Q2008 166 2008 208 L1998 462 Q1996 507 1950 507 Q1122 479 295 507 Q249 507 247 462 L237 208 Q237 166 282 163 Z"/>
  <path class="safe-line" d="M300 188 Q1120 162 1940 188 Q1985 190 1985 220 L1978 462 Q1976 484 1945 484 Q1122 456 300 484 Q270 484 268 462 L262 220 Q262 190 300 188 Z"/>
  <path class="label-frame" d="M310 212 Q1122 192 1938 212 Q1960 213 1960 235 L1958 440 Q1957 460 1938 460 Q1122 434 310 460 Q291 460 290 440 L287 235 Q287 213 310 212 Z"/>

  <!-- maker block -->
  <g class="body-text maker" transform="rotate(-1.3 430 300)">
    <text class="maker-title" x="310" y="258">Manufactured for:</text>
    <text class="maker-line" x="310" y="281">Millbrook Labs Corporation</text>
    <text class="maker-line" x="311" y="304">For: The Fern Brands</text>
    <text class="maker-line" x="312" y="327">240 Harlow Ridge Lane Suite 12</text>
    <text class="maker-line" x="313" y="350">Fairview, TN 37999</text>
    <rect class="info-box" x="316" y="371" width="248" height="66"/>
    <text class="exp-label" x="326" y="392">Exp. Date:</text>
  </g>

  <!-- benefits -->
  <g class="body-text benefits" transform="rotate(-0.8 730 330)">
    <text class="benefit" x="586" y="250">• Strengthens skin hydration</text>
    <text class="benefit" x="587" y="283">• Increases skin elasticity</text>
    <text class="benefit" x="588" y="316">• Stimulates skin cell growth</text>
    <text class="benefit" x="589" y="349">• Anti-wrinkle effect</text>
    <text class="benefit" x="590" y="382">• Antioxidant enhancer</text>
    <text class="benefit" x="591" y="415">• Improvement of ageing spots</text>
  </g>

  <!-- brand panel -->
  <g class="brand-panel" text-anchor="middle">
    <circle class="brand-ring" cx="1122" cy="237" r="19"/>
    <text class="body-text brand-by" x="1124" y="269">BY · DR VELLO</text>
    <text class="product-name" x="1124" y="325">ALVA</text>
    <text class="body-text product-type" x="1124" y="342">ANTI-AGING MOISTURIZER</text>
    <text class="net-weight" x="1124" y="378">4Oz</text>
    <text class="body-text made-with" x="1123" y="401">MADE WITH</text>
    <text class="body-text key-extract" x="1123" y="417">PHYTOPLANKTON EXTRACT</text>
  </g>

  <!-- ingredients -->
  <g class="ingredients-block" transform="rotate(1.2 1590 330)">
    <text class="ingredients" x="1388" y="250" textLength="410">Ingredients: deionized water, cocos nucifera, stearic acid, emulsifying</text>
    <text class="ingredients" x="1388" y="277" textLength="404">wax, hyaluronic acid, citric acid, glycerin, populous tremuloides bark</text>
    <text class="ingredients" x="1388" y="304" textLength="366">extract, plankton extract (nannochloropsis gaditana, isochrysis</text>
    <text class="ingredients" x="1388" y="331" textLength="386">galbana, phaeodactylum tricornutum, tetraselmis chuii, dunaliella</text>
    <text class="ingredients" x="1388" y="358" textLength="373">salina), plankton powder, (nannochloropsis gaditana, isochrysis</text>
    <text class="ingredients" x="1388" y="385" textLength="386">galbana, phaeodactylum tricornutum, tetraselmis chuii, dunaliella</text>
    <text class="ingredients" x="1388" y="412" textLength="326">salina), lonicera caprifolium (honeysuckle absolute oil).</text>
  </g>
  <rect class="info-box code-box" x="1815" y="225" width="133" height="219" transform="rotate(1 1881 334)"/>
</svg>
</body>
</html>
```